Brantwell Group needs a business card design

We need a new business card design using the logo recently selected in a logo competition on Pixel Forum. Our business is a consultancy specializing in aviation and energy and the winning business card design will promote an image of precision and professionalism with creativity.

Please use the logo with the name on the front of the card and use a complementary font. Make the back white with either the light grey or dark grey logo.

Target Market(s)

Senior finance and legal leaders at aviation and energy companies

Industry/Entity Type

Management Consulting

Contact Information for Business Card

Peter Haldane
President
Brantwell Group

www.brantwellgroup.example

(555) 304-6198
ph@brantwellgroup.example

Requirements
Must have
• Professional font that goes well with the logo font

```html
<!DOCTYPE html>
<html lang="en">
<head>
<meta charset="utf-8">
<title>Brantwell Group — Business Card</title>
<link rel="stylesheet" href="https://fonts.googleapis.com/css2?family=Open+Sans:wght@400;600;700&display=swap">
<style>
  :root {
    --navy: #1a4f7e;
    --navy-deep: #123a60;
    --steel: #5a6470;
    --grey-band: #6b7078;
    --lavender: #dcdfeb;
    --lavender-light: #eceef5;
    --paper: #ffffff;
    --backdrop: #eef0f3;
    --text-muted: #8a8f98;
  }
  * { margin: 0; padding: 0; box-sizing: border-box; }
  html, body { width: 1200px; height: 913px; overflow: hidden; }
  body {
    background: var(--backdrop);
    font-family: "Open Sans", Arial, sans-serif;
    display: flex;
    align-items: center;
    justify-content: center;
    gap: 60px;
  }
  .card {
    position: relative;
    width: 540px;
    height: 309px;
    overflow: hidden;
    box-shadow: 0 6px 18px rgba(20, 30, 50, 0.18);
  }
  .card--front { background: linear-gradient(160deg, var(--lavender-light), var(--lavender)); }
  .card--back { background: var(--paper); }
  .card__bands { position: absolute; inset: 0; width: 100%; height: 100%; }

  .brand {
    position: absolute;
    display: flex;
    align-items: center;
    gap: 10px;
    color: var(--navy);
    font-weight: 600;
    white-space: nowrap;
  }
  .brand__mark { background: var(--navy); flex: none; }
  .card--front .brand { left: 48px; top: 78px; font-size: 26px; }
  .card--front .brand__mark { width: 16px; height: 16px; }
  .card--back .brand { left: 50%; top: 104px; transform: translateX(-50%); font-size: 38px; }
  .card--back .brand__mark { width: 22px; height: 22px; }

  .person { position: absolute; right: 36px; top: 112px; text-align: right; }
  .person__name { color: var(--navy); font-weight: 700; font-size: 20px; line-height: 1.1; }
  .person__title { color: var(--text-muted); font-size: 12px; margin-top: 2px; }
  .divider {
    position: absolute; left: 36px; right: 30px; top: 160px;
    height: 1px; background: var(--navy);
  }

  .contacts { position: absolute; left: 48px; top: 180px; list-style: none; }
  .contacts li {
    display: flex; align-items: center; gap: 8px;
    color: var(--navy); font-size: 13px; line-height: 20px;
  }
  .contacts svg { width: 10px; height: 10px; fill: var(--steel); flex: none; }
</style>
</head>
<body>

  <section class="card card--front" aria-label="Business card front">
    <svg class="card__bands" viewBox="0 0 540 309" preserveAspectRatio="none" aria-hidden="true">
      <rect x="0" y="270" width="540" height="39" fill="var(--grey-band)"/>
      <polygon points="395,228 540,228 540,309 410,309 410,262" fill="var(--navy)"/>
    </svg>
    <div class="brand"><span class="brand__mark"></span>Brantwell Group</div>
    <div class="person">
      <p class="person__name">Peter Haldane</p>
      <p class="person__title">President</p>
    </div>
    <div class="divider"></div>
    <ul class="contacts">
      <li>
        <svg viewBox="0 0 10 10"><path d="M2 0.5 L3.6 0.5 L4.2 2.8 L3 3.6 Q4 6 6.4 7 L7.2 5.8 L9.5 6.4 L9.5 8 Q9.5 9.5 8 9.5 Q0.5 9 0.5 2 Q0.5 0.5 2 0.5 Z"/></svg>
        (555) 304-6198
      </li>
      <li>
        <svg viewBox="0 0 10 10"><path d="M0.5 2 H9.5 V8.5 H0.5 Z M1.2 2.6 L5 5.6 L8.8 2.6" fill="none" stroke="var(--steel)" stroke-width="1"/></svg>
        ph@brantwellgroup.example
      </li>
      <li>
        <svg viewBox="0 0 10 10"><circle cx="5" cy="5" r="4.5"/><path d="M0.5 5 H9.5 M5 0.5 V9.5" stroke="var(--lavender)" stroke-width="0.8"/></svg>
        www.brantwellgroup.example
      </li>
    </ul>
  </section>

  <section class="card card--back" aria-label="Business card back">
    <svg class="card__bands" viewBox="0 0 540 309" preserveAspectRatio="none" aria-hidden="true">
      <rect x="0" y="262" width="540" height="47" fill="var(--grey-band)"/>
      <polygon points="0,240 300,240 312,252 300,262 300,309 0,309" fill="var(--navy-deep)"/>
    </svg>
    <div class="brand"><span class="brand__mark"></span>Brantwell Group</div>
  </section>

</body>
</html>
```